Towing Company Website Towing Bergfeld Ost

Hello I need a cool website for my towing company. - Home - About us - Parking Enforcement - Repossession - Disaster Recovery - Accident Recovery - Contact So someone would have to install the website on Hostarly for me. No idea how that works.

Target Market(s)

www.bergungsfix.cc

Contact Information for Business Card

Bergungsfix Talwiesen Ost
P: 044 736 48 91
F: 044 736 48 97
E: mail@bergungsfix.cc
W: www.bergungsfix.cc

Lukas Vontobel
M: 075 628 94 17

Number of Pages Required

5+ page

Font styles to use
Sans Serif

Colors

Designer to choose colors to be used in the design.

```html
<!DOCTYPE html>
<html lang="en">
<head>
<meta charset="utf-8">
<title>Bergungsfix Talwiesen Ost – Towing Bergfeld Ost</title>
<link href="https://fonts.googleapis.com/css2?family=Roboto:wght@400;500;700;900&family=Roboto+Slab:wght@700&display=swap" rel="stylesheet">
<style>
:root{
  --red:#d7141f;
  --navy:#1b3a6b;
  --navy-dark:#142c55;
  --ink:#222428;
  --dark:#17181c;
  --card:#1d2430;
  --grey:#6f7277;
  --light:#f4f5f7;
  --sky:#dde9f6;
  --white:#ffffff;
}
*{box-sizing:border-box;margin:0;padding:0}
html,body{width:1200px;height:5070px;overflow:hidden}
body{font-family:"Roboto",Arial,sans-serif;color:var(--ink);background:var(--white);position:relative}
.abs{position:absolute}
.brand{font-family:"Roboto Slab",Georgia,serif;font-weight:700;color:var(--ink)}
/* header */
.topbar{top:0;left:0;width:1200px;height:128px;background:var(--white)}
.call{left:130px;top:36px;display:flex;align-items:center;gap:14px}
.call-icon{width:44px;height:44px;border-radius:50%;background:var(--red);display:flex;align-items:center;justify-content:center}
.call small{display:block;font-size:15px;color:var(--ink)}
.call strong{display:block;font-size:26px;color:var(--red);font-weight:700}
.logo{left:430px;top:18px;width:340px;text-align:center;display:flex;align-items:center;justify-content:center;gap:10px}
.logo-mark{width:22px;height:22px;background:var(--red)}
.logo .brand{font-size:25px;line-height:1.15;text-align:left}
.search{left:820px;top:38px;width:245px;height:38px;border:1px solid #cfd2d6;border-radius:19px;display:flex;align-items:center;justify-content:space-between;padding:0 14px;font-size:13px;color:#999}
.nav{top:128px;left:0;width:1200px;height:48px;background:var(--navy);display:flex;justify-content:center;align-items:center;gap:32px}
.nav a{color:var(--white);text-decoration:none;font-size:15px;font-weight:500;text-transform:uppercase}
/* hero */
.hero{top:176px;left:0;width:1200px;height:524px;background:linear-gradient(100deg,#5f6f62 0%,#8d9aa3 35%,#c4ccd2 60%,#6c7a66 100%)}
.hero-title{left:270px;top:200px;width:660px;padding:14px 20px 14px 70px;background:rgba(255,255,255,.82);text-align:center;font-size:46px;line-height:1.05;font-weight:900;color:var(--navy-dark);text-transform:uppercase}
.hero-title svg{position:absolute;left:0;top:-6px}
.arrow-btn{width:44px;height:52px;background:rgba(255,255,255,.85);display:flex;align-items:center;justify-content:center}
/* welcome */
.welcome{top:780px;left:115px;width:440px}
.welcome h3{color:var(--red);font-size:24px;font-weight:700;text-align:right;padding-right:100px}
.welcome .brand{font-size:34px;line-height:1.15;margin:6px 0 24px 0;display:flex;gap:12px;align-items:center}
.welcome p{font-size:15px;line-height:1.85;color:var(--grey)}
.video{left:620px;top:812px;width:380px;height:302px;background:linear-gradient(160deg,#6d7480,#3d4148 55%,#a5a9ae);box-shadow:0 4px 14px rgba(0,0,0,.25)}
.play{left:790px;top:943px;width:50px;height:36px;border-radius:9px;background:var(--red);display:flex;align-items:center;justify-content:center}
/* dark band */
.darkband{top:1380px;left:0;width:1200px;height:880px}
.truck{left:255px;top:1240px;width:780px;height:280px;background:radial-gradient(ellipse at center,#eef0f3 0%,#c9ced6 55%,rgba(255,255,255,0) 72%)}
.helps{top:1590px;left:0;width:1200px;text-align:center;color:var(--white)}
.helps .bar{width:60px;height:3px;background:var(--white);margin:0 auto 22px}
.helps h2{font-size:29px;font-weight:700;text-transform:uppercase}
.helps p{font-size:29px;text-transform:uppercase;font-weight:400;margin-top:6px}
.feature{width:305px;border:2px solid var(--white);background:var(--card);color:var(--white);text-align:center;padding:60px 18px 0}
.feature.white{background:var(--white);color:var(--ink);border-color:var(--white)}
.feature h4{font-size:17px;font-weight:700;text-transform:uppercase;margin-bottom:14px}
.feature p{font-size:13.5px;line-height:1.75}
.feature .ic{position:absolute;left:50%;top:-40px;margin-left:-40px;width:80px;height:80px;border-radius:50%;background:var(--red);border:4px solid var(--white);display:flex;align-items:center;justify-content:center}
.more{position:absolute;left:50%;bottom:-18px;transform:translateX(-50%);background:var(--red);color:var(--white);font-size:13px;font-weight:700;padding:10px 24px;border-radius:20px;white-space:nowrap;text-transform:uppercase}
/* section heading */
.sec-head{left:0;width:1200px;text-align:center}
.sec-head .bar{width:60px;height:3px;background:var(--red);margin:0 auto 22px}
.sec-head h2{font-size:38px;font-weight:400;text-transform:uppercase;color:var(--ink)}
.sec-head h2 b{font-weight:900}
/* services */
.service{width:455px;height:330px;background:var(--white);box-shadow:0 3px 12px rgba(0,0,0,.18);border-bottom:4px solid var(--red)}
.service .ph{height:200px}
.service svg.tri{position:absolute;left:0;top:175px}
.service h5{position:absolute;left:100px;top:218px;font-size:18px;font-weight:700;text-transform:uppercase}
.service p{position:absolute;left:100px;top:248px;width:330px;font-size:13.5px;line-height:1.65;color:var(--grey)}
/* newsletter */
.newsletter{top:3330px;left:0;width:1200px;height:570px;background:var(--sky)}
.newsletter .sub{top:3478px;width:1200px;text-align:center;font-size:15px;color:var(--grey)}
.field{height:42px;background:var(--white);border:1px solid #c9d2dc;font-size:13px;color:#888;display:flex;align-items:center;padding-left:18px}
.btn-red{background:var(--red);color:var(--white);font-weight:700;font-size:17px;display:flex;align-items:center;justify-content:center}
.scene{top:3605px;left:0;width:1200px;height:295px;background:linear-gradient(180deg,#dde9f6 0%,#b4c6dc 45%,#9aaec8 78%,#6c7886 100%)}
/* clients */
.testi{width:290px;font-size:14px;line-height:1.6;color:var(--grey)}
.testi .q{font-size:54px;color:#c5c7ca;line-height:.6;font-family:Georgia,serif;display:block;height:26px}
.who{display:flex;align-items:center;gap:16px;margin-top:20px}
.avatar{width:64px;height:64px;border-radius:50%;background:linear-gradient(160deg,#b8bdc3,#6e747b)}
.who b{display:block;color:var(--red);font-size:16px}
.who span{display:block;color:var(--ink);font-size:14px}
.stars{color:var(--red);font-size:15px;letter-spacing:2px}
.cnav{width:28px;height:28px;border-radius:50%;background:#4a4d52;display:flex;align-items:center;justify-content:center}
/* footer */
.footer{top:4440px;left:0;width:1200px;height:630px}
.fcol h3{font-size:23px;font-weight:700;color:var(--white);text-transform:uppercase}
.fcol .bar{width:44px;height:3px;background:var(--white);margin:14px 0 30px}
.ffield{width:365px;height:34px;border:1px solid #666a70;color:#cfd1d4;font-size:12px;padding-left:10px;display:flex;align-items:center;margin-bottom:12px}
.ffield.msg{height:64px;align-items:flex-start;padding-top:8px}
.submit{width:176px;height:34px;background:var(--red);color:var(--white);font-weight:700;font-size:16px;display:flex;align-items:center;justify-content:center;text-transform:uppercase}
.crow{display:flex;gap:16px;color:var(--white);font-size:14.5px;line-height:1.55;margin-bottom:20px}
.cic{width:34px;height:34px;border-radius:50%;border:1px solid #8f9398;flex:none;display:flex;align-items:center;justify-content:center}
.social{display:flex;gap:8px;margin-left:0}
.social i{width:26px;height:26px;border-radius:50%;border:1px solid #cfd1d4;display:block}
.links a{display:block;color:var(--white);text-decoration:none;font-size:14.5px;line-height:1.95}
.copy{top:5016px;width:1200px;text-align:center;color:#cfd1d4;font-size:14px}
.rule{top:4985px;left:135px;width:930px;height:1px;background:#3a3d42}
</style>
</head>
<body>

<!-- header -->
<header class="abs topbar">
  <div class="abs call">
    <div class="call-icon"><svg width="20" height="20" viewBox="0 0 24 24"><path fill="#fff" d="M6.6 10.8a15.5 15.5 0 0 0 6.6 6.6l2.2-2.2c.3-.3.7-.4 1-.2 1.1.4 2.3.6 3.6.6.6 0 1 .4 1 1V20c0 .6-.4 1-1 1A17 17 0 0 1 3 4c0-.6.4-1 1-1h3.5c.6 0 1 .4 1 1 0 1.3.2 2.5.6 3.6.1.3 0 .7-.2 1z"/></svg></div>
    <div><small>Have any Question?</small><strong>0447364891</strong></div>
  </div>
  <div class="abs logo"><span class="logo-mark"></span><div class="brand">Bergungsfix<br>Talwiesen Ost</div></div>
  <div class="abs search">Search here <svg width="16" height="16" viewBox="0 0 24 24"><circle cx="10" cy="10" r="7" fill="none" stroke="#666" stroke-width="2.4"/><path d="M15 15l6 6" stroke="#666" stroke-width="2.4"/></svg></div>
</header>
<nav class="abs nav">
  <a href="#">Home</a><a href="#">About us</a><a href="#">Parking Enforcement</a><a href="#">Repossession</a><a href="#">Breakdown Assistance</a><a href="#">Accident Recovery</a><a href="#">Contact us</a>
</nav>

<!-- hero -->
<section class="abs hero" role="img" aria-label="Photo: a man on the phone beside a broken-down white car on a roadside, a tow truck behind"></section>
<div class="abs hero-title" style="top:376px">
  <svg width="70" height="120" viewBox="0 0 70 120"><path d="M4 116L40 8l26 108z" fill="none" stroke="#d7141f" stroke-width="8"/></svg>
  Towing Bergfeld Ost<br>helps in every situation
</div>
<div class="abs arrow-btn" style="left:0;top:414px"><svg width="14" height="20"><path d="M11 2L3 10l8 8" fill="none" stroke="#333" stroke-width="3"/></svg></div>
<div class="abs arrow-btn" style="left:1156px;top:414px"><svg width="14" height="20"><path d="M3 2l8 8-8 8" fill="none" stroke="#333" stroke-width="3"/></svg></div>

<!-- welcome -->
<section class="abs welcome">
  <h3>Welcome to</h3>
  <div class="brand"><span class="logo-mark"></span>Bergungsfix Talwiesen Ost</div>
  <p>Sed ut perspiciatis unde omnis iste natus error sit voluptatem accusantium doloremque laudantium, totam rem aperiam, eaque ipsa quae ab illo inventore veritatis et quasi architecto beatae vitae dicta sunt explicabo. Nemo enim ipsam voluptatem quia voluptas sit aspernatur aut odit aut fugit, sed quia consequuntur magni dolores eos qui ratione voluptatem sequi nesciunt.</p>
</section>
<div class="abs video" role="img" aria-label="Video still: a person looking into the open bonnet of a car"></div>
<div class="abs play"><svg width="16" height="16"><path d="M3 1l12 7-12 7z" fill="#fff"/></svg></div>

<!-- dark band -->
<svg class="abs darkband" width="1200" height="880" viewBox="0 0 1200 880">
  <polygon points="0,0 1200,80 1200,800 0,860" fill="#17181c"/>
  <polygon points="0,0 700,50 0,160" fill="#26282d"/>
  <polygon points="1200,80 1200,300 520,130" fill="#26282d"/>
  <polygon points="0,860 1200,800 1200,880 0,880" fill="#ffffff"/>
</svg>
<div class="abs truck" role="img" aria-label="Illustration: white and blue flatbed tow truck"></div>
<section class="abs helps">
  <div class="bar"></div>
  <h2>Towing Bergfeld Ost helps</h2>
  <p>in every situation</p>
</section>

<div class="abs feature" style="left:115px;top:1765px;height:280px">
  <div class="ic"><svg width="40" height="30" viewBox="0 0 40 30"><path d="M2 22h6l4-10h12l4 10h10v-4l-6-6" fill="none" stroke="#fff" stroke-width="2.5"/><circle cx="11" cy="24" r="4" fill="#fff"/><circle cx="30" cy="24" r="4" fill="#fff"/></svg></div>
  <h4>Tow away</h4>
  <p>Your parking space is constantly blocked by third-party, wrong or long-term parkers? Act instead of getting angry! We check your parking spaces, entrances and exits, fire brigade and</p>
  <span class="more">Read more</span>
</div>
<div class="abs feature white" style="left:447px;top:1800px;height:285px">
  <div class="ic"><svg width="36" height="34" viewBox="0 0 36 34"><rect x="3" y="8" width="22" height="16" fill="none" stroke="#fff" stroke-width="2.5"/><path d="M25 13h6l3 5v6h-9" fill="none" stroke="#fff" stroke-width="2.5"/><circle cx="10" cy="28" r="3.5" fill="#fff"/><circle cx="28" cy="28" r="3.5" fill="#fff"/></svg></div>
  <h4>Free parking!</h4>
  <p>We monitor your parking around the clock. We are where wrong, foreign and long-term parker problems - we solve them immediately. With our service, we ensure the satisfaction</p>
  <span class="more">Read more</span>
</div>
<div class="abs feature" style="left:780px;top:1765px;height:280px">
  <div class="ic"><svg width="34" height="34" viewBox="0 0 34 34"><path d="M4 4h13l13 13-13 13L4 17z" fill="#fff"/><circle cx="11" cy="11" r="3" fill="#d7141f"/></svg></div>
  <h4>Transparent prices</h4>
  <p>Empty journey Fr. 200.- Empty journey - only (Without any work on site)<br>Towing Fr. 400.- All inclusive<br>(Car vehicles up to 2t)<br>Stand costs Fr. 50.- daily rate</p>
  <span class="more">Read more</span>
</div>

<!-- services -->
<div class="abs sec-head" style="top:2340px">
  <div class="bar"></div>
  <h2><b>Our</b> Services</h2>
</div>
<article class="abs service" style="left:135px;top:2487px">
  <div class="ph" role="img" aria-label="Photo: parking warden in a high-visibility vest writing a ticket" style="background:linear-gradient(150deg,#8f9b7a,#c7c9b0 50%,#5d6a5a)"></div>
  <svg class="tri" width="95" height="120" viewBox="0 0 95 120"><path d="M8 112L48 10l40 102z" fill="#fff" stroke="#d7141f" stroke-width="8"/></svg>
  <h5>Parking Enforcement</h5>
  <p>Sed ut perspiciatis unde omnis iste natus voluptatem accusantium doloremque laudantium, totam</p>
</article>
<article class="abs service" style="left:615px;top:2487px">
  <div class="ph" role="img" aria-label="Photo: damaged cars on a street being repossessed" style="background:linear-gradient(150deg,#7f8b78,#d2d4d0 50%,#5d6166)"></div>
  <svg class="tri" width="95" height="120" viewBox="0 0 95 120"><path d="M8 112L48 10l40 102z" fill="#fff" stroke="#d7141f" stroke-width="8"/></svg>
  <h5>Repossession</h5>
  <p>Sed ut perspiciatis unde omnis iste natus voluptatem accusantium doloremque laudantium, totam</p>
</article>
<article class="abs service" style="left:135px;top:2847px">
  <div class="ph" role="img" aria-label="Photo: driver on the phone next to a broken-down car" style="background:linear-gradient(150deg,#a0a7a8,#d9dcdf 50%,#6d747a)"></div>
  <svg class="tri" width="95" height="120" viewBox="0 0 95 120"><path d="M8 112L48 10l40 102z" fill="#fff" stroke="#d7141f" stroke-width="8"/></svg>
  <h5>Breakdown Assistance</h5>
  <p>Sed ut perspiciatis unde omnis iste natus voluptatem accusantium doloremque laudantium, totam</p>
</article>
<article class="abs service" style="left:615px;top:2847px">
  <div class="ph" role="img" aria-label="Photo: two people beside a crashed car after an accident" style="background:linear-gradient(150deg,#6f7c70,#aeb4b0 50%,#4c5358)"></div>
  <svg class="tri" width="95" height="120" viewBox="0 0 95 120"><path d="M8 112L48 10l40 102z" fill="#fff" stroke="#d7141f" stroke-width="8"/></svg>
  <h5>Accident Recovery</h5>
  <p>Sed ut perspiciatis unde omnis iste natus voluptatem accusantium doloremque laudantium, totam</p>
</article>

<!-- newsletter -->
<section class="abs newsletter"></section>
<div class="abs sec-head" style="top:3393px">
  <div class="bar"></div>
  <h2><b>Sign up for</b> Newsletter</h2>
</div>
<p class="abs sub newsletter-sub" style="top:3478px;left:0;width:1200px;text-align:center;font-size:15px;color:#6f7277">Factsheet Cantonal police Bergfeld Towing from private property</p>
<div class="abs field" style="left:233px;top:3525px;width:280px">Enter your Name</div>
<div class="abs field" style="left:522px;top:3525px;width:275px">Enter your business email</div>
<div class="abs btn-red" style="left:808px;top:3525px;width:165px;height:42px">Download PDF</div>
<div class="abs scene" role="img" aria-label="Illustration: city skyline, a red car loaded onto a flatbed tow truck, a no-parking sign and two people"></div>

<!-- clients -->
<div class="abs sec-head" style="top:3990px">
  <div class="bar"></div>
  <h2><b>Our clients says</b></h2>
</div>
<div class="abs cnav" style="left:70px;top:4200px"><svg width="10" height="12"><path d="M8 1L2 6l6 5" fill="none" stroke="#fff" stroke-width="2"/></svg></div>
<div class="abs cnav" style="left:1088px;top:4200px"><svg width="10" height="12"><path d="M2 1l6 5-6 5" fill="none" stroke="#fff" stroke-width="2"/></svg></div>

<div class="abs testi" style="left:135px;top:4135px">
  <span class="q">&ldquo;</span>Sed ut perspiciatis unde omnis iste natus error sit voluptatem accusantium doloremque laudantium, totam rem aperiam, eaque ipsa quae ab illo inventore
  <div class="who"><div class="avatar" role="img" aria-label="Client portrait"></div><div><b>Nora K. Meier</b><span>Bergungsfix</span><span class="stars">★★★★★</span></div></div>
</div>
<div class="abs testi" style="left:470px;top:4135px">
  <span class="q">&ldquo;</span>Sed ut perspiciatis unde omnis iste natus error sit voluptatem accusantium doloremque laudantium, totam rem aperiam, eaque ipsa quae ab illo inventore
  <div class="who"><div class="avatar" role="img" aria-label="Client portrait"></div><div><b>Nora K. Meier</b><span>Bergungsfix</span><span class="stars">★★★★★</span></div></div>
</div>
<div class="abs testi" style="left:800px;top:4135px">
  <span class="q">&ldquo;</span>Sed ut perspiciatis unde omnis iste natus error sit voluptatem accusantium doloremque laudantium, totam rem aperiam, eaque ipsa quae ab illo inventore
  <div class="who"><div class="avatar" role="img" aria-label="Client portrait"></div><div><b>Nora K. Meier</b><span>Bergungsfix</span><span class="stars">★★★★★</span></div></div>
</div>

<!-- footer -->
<svg class="abs footer" width="1200" height="630" viewBox="0 0 1200 630">
  <polygon points="0,30 1200,0 1200,630 0,630" fill="#17181c"/>
  <polygon points="0,30 520,17 0,110" fill="#1b3a6b"/>
  <polygon points="1200,0 1200,60 700,12" fill="#1b3a6b"/>
</svg>
<div class="abs fcol" style="left:155px;top:4560px">
  <h3>E-mail us</h3><div class="bar"></div>
  <div class="ffield">First Name</div>
  <div class="ffield">Email Address</div>
  <div class="ffield">Phone Number</div>
  <div class="ffield msg">Message</div>
  <div class="submit">Submit</div>
</div>
<div class="abs fcol" style="left:590px;top:4560px">
  <h3>Contact us</h3><div class="bar"></div>
  <div class="crow"><div class="cic"><svg width="14" height="16" viewBox="0 0 14 18"><path d="M7 1a6 6 0 0 0-6 6c0 4.5 6 10 6 10s6-5.5 6-10a6 6 0 0 0-6-6z" fill="#fff"/><circle cx="7" cy="7" r="2.2" fill="#17181c"/></svg></div><div>Towing Bergfeld Ost<br>Talstrasse 24, 8155 Bergfeld,<br>Switzerland</div></div>
  <div class="crow"><div class="cic"><svg width="14" height="14" viewBox="0 0 24 24"><path fill="#fff" d="M6.6 10.8a15.5 15.5 0 0 0 6.6 6.6l2.2-2.2c.3-.3.7-.4 1-.2 1.1.4 2.3.6 3.6.6.6 0 1 .4 1 1V20c0 .6-.4 1-1 1A17 17 0 0 1 3 4c0-.6.4-1 1-1h3.5c.6 0 1 .4 1 1 0 1.3.2 2.5.6 3.6.1.3 0 .7-.2 1z"/></svg></div><div>Phone:<br>0447364891</div></div>
  <div class="crow"><div class="cic"><svg width="16" height="12" viewBox="0 0 16 12"><rect x="1" y="1" width="14" height="10" fill="none" stroke="#fff" stroke-width="1.6"/><path d="M1 1l7 6 7-6" fill="none" stroke="#fff" stroke-width="1.6"/></svg></div><div>Email:<br>mail@bergungsfix.cc</div></div>
  <div class="social"><i></i><i></i><i></i><i></i></div>
</div>
<div class="abs fcol links" style="left:912px;top:4560px">
  <h3>Quick links</h3><div class="bar"></div>
  <a href="#">Home</a><a href="#">About us</a><a href="#">Parking Enforcement</a><a href="#">Repossession</a><a href="#">Breakdown Assistance</a><a href="#">Accident Recovery</a><a href="#">Contact</a>
</div>
<div class="abs rule"></div>
<p class="abs copy">© Copyright 2019 Bergungsfix Talwiesen Ost. All Rights Reserved.</p>

</body>
</html>
```